The Steady Climb Podcast Cover Art

I'm upgrading my podcast cover art to a new design. The show is called The Steady Climb and we interview guests who have gone through different challenges/adversities that we face in life. During the interview, we unpack how they've gotten past the adversity and how that insight might help others. I will link the show and old cover art. I will upload a new photo or two that can be used for the new cover art.

Look at previous cover for items that needed on the cover like Podvara, wavlio etc.

Should also have a small caption that states
“UNTOLD STORIES OF EVERYDAY ADVERSITY & PERSEVERANCE”

Wavlio: https://listen.wavlio-example.net/show/7QR2k4LdPzHwXnBTVmcaF9?si=ra4Xk8Tpqe-W27YbCvhnpL

Target Market(s)

Podcast learning community

Industry/Entity Type

Podcast, Education

Colors
EB3D1F
EC4F4E
F09395
F8D3D4
FCEDEE

Requirements
Must have
• RM Logo, Colors are red, black and white.

```html
<!DOCTYPE html>
<html lang="en">
<head>
<meta charset="utf-8">
<title>The Steady Climb – Podcast Cover</title>
<link href="https://fonts.googleapis.com/css2?family=Montserrat:wght@400;600;700;900&family=Oswald:wght@400&family=Great+Vibes&display=swap" rel="stylesheet">
<style>
  :root {
    --stage: #5f5f5f;
    --ink: #0a0a0a;
    --red: #e41e2b;
    --white: #ffffff;
    --badge: #121212;
    --panel: rgba(255, 255, 255, 0.86);
  }
  html, body {
    margin: 0;
    width: 1200px;
    height: 1000px;
    overflow: hidden;
    background: var(--stage);
  }
  .cover {
    position: absolute;
    left: 145px;
    top: 86px;
    width: 761px;
    height: 761px;
    overflow: hidden;
    background: var(--ink);
    font-family: "Montserrat", sans-serif;
  }
  .host-photo {
    position: absolute;
    inset: 0;
    background:
      radial-gradient(ellipse 40% 32% at 46% 30%, #8a5a3e 0%, rgba(138,90,62,0) 100%),
      radial-gradient(ellipse 55% 38% at 50% 62%, #bdbdbd 0%, rgba(189,189,189,0) 100%),
      linear-gradient(90deg, #6b4f3a 0%, #2a211b 28%, #0b0b0b 55%, #050505 100%);
  }
  .host-photo::after {
    content: "";
    position: absolute;
    inset: 0;
    background: linear-gradient(180deg, rgba(0,0,0,0) 55%, rgba(0,0,0,0.9) 74%, #000 100%);
  }
  .brand-panel {
    position: absolute;
    left: 0;
    top: 0;
    width: 303px;
    height: 283px;
    background: var(--panel);
    display: flex;
    align-items: center;
    justify-content: center;
  }
  .brand-name {
    font-weight: 600;
    font-size: 26px;
    letter-spacing: 1px;
    color: var(--red);
    white-space: nowrap;
  }
  .title-kicker {
    position: absolute;
    left: 59px;
    top: 482px;
    margin: 0;
    font-weight: 900;
    font-size: 38px;
    letter-spacing: 5px;
    color: var(--white);
    line-height: 1;
  }
  .title-main {
    position: absolute;
    left: 40px;
    top: 520px;
    margin: 0;
    font-weight: 900;
    font-size: 72px;
    letter-spacing: 1px;
    color: var(--red);
    line-height: 1;
    white-space: nowrap;
  }
  .host-line {
    position: absolute;
    right: 40px;
    top: 588px;
    margin: 0;
    font-family: "Great Vibes", cursive;
    font-size: 54px;
    color: var(--white);
    line-height: 1;
    white-space: nowrap;
  }
  .listen-badge {
    position: absolute;
    top: 616px;
    height: 54px;
    background: var(--badge);
    display: flex;
    align-items: center;
    gap: 8px;
    padding: 0 9px;
    box-sizing: border-box;
    color: var(--white);
  }
  .listen-badge--wavlio { left: 35px; width: 160px; }
  .listen-badge--podvara { left: 209px; width: 150px; }
  .badge-dot {
    width: 32px;
    height: 32px;
    border-radius: 50%;
    background: var(--white);
    flex: none;
  }
  .badge-text { display: flex; flex-direction: column; line-height: 1; }
  .badge-lead { font-size: 11px; font-weight: 600; margin-bottom: 3px; }
  .badge-name { font-size: 22px; font-weight: 600; }
  .tagline {
    position: absolute;
    left: 0;
    right: 0;
    top: 695px;
    margin: 0;
    text-align: center;
    font-family: "Oswald", sans-serif;
    font-size: 28px;
    letter-spacing: 0.4px;
    color: var(--white);
    line-height: 1;
    white-space: nowrap;
  }
</style>
</head>
<body>
  <main class="cover">
    <div class="host-photo" role="img" aria-label="Photo of the host in a grey turtleneck wearing headphones, seated at a studio microphone"></div>

    <div class="brand-panel">
      <span class="brand-name">REID MARLOWE</span>
    </div>

    <h1 class="title-kicker">THE</h1>
    <h2 class="title-main">STEADY CLIMB</h2>
    <p class="host-line">with Reid Marlowe</p>

    <div class="listen-badge listen-badge--wavlio">
      <span class="badge-dot"></span>
      <span class="badge-text">
        <span class="badge-lead">Listen On</span>
        <span class="badge-name">Wavlio</span>
      </span>
    </div>

    <div class="listen-badge listen-badge--podvara">
      <span class="badge-dot"></span>
      <span class="badge-text">
        <span class="badge-lead">Available on</span>
        <span class="badge-name">Podvara</span>
      </span>
    </div>

    <p class="tagline">“UNTOLD STORIES OF EVERYDAY ADVERSITY &amp; PERSEVERANCE”</p>
  </main>
</body>
</html>
```